Creating a visual for the various stage of our Packets by Locations: *Memphis Region *Clinics in TRV School District*Nashville Region *Knoxville Region. The attached file contains two tabs the layout of the packet scheme that currently in place and a second tab with the definition of the various cells that is needed as a legend on each report. The goal is to get the report tab an easily "eye" visual for the CEO of the company to follow. Create a Reporting Dashboard Template that we can input number into easily to update. The color scheme should reflect our website www.brightsprout.example
Target Market(s)
Pediatric company that performs Bright Sprout Exams and Optometry exams in school districts
Industry/Entity Type
Healthcare
Requirements
Must have
- Printable dash page. You can use this file and add a dash page that flows from the report page as an option in excel
Nice to have
- maybe 3D modern feel with the color scheme of the company website

```html
<!DOCTYPE html>
<html lang="en">
<head>
<meta charset="utf-8">
<title>Bright Sprout Packet Reporting Dashboard</title>
<link href="https://fonts.googleapis.com/css2?family=Montserrat:wght@500;600;700;800&family=Open+Sans:wght@400;600;700&display=swap" rel="stylesheet">
<style>
:root{
  --stage:#ebebeb;
  --navy:#1b3170;
  --blue:#1f5fb8;
  --blue-dark:#184d9c;
  --blue-light:#1e88e5;
  --red:#d32027;
  --yellow:#f2b705;
  --green:#13967a;
  --teal:#3cc7cf;
  --ink:#222;
  --paper:#fff;
  --panel-grey:#f1f1f1;
}
*{box-sizing:border-box;margin:0;padding:0}
html,body{width:775px;height:1200px;overflow:hidden;background:var(--stage)}
body{position:relative;font-family:"Open Sans",sans-serif;color:var(--ink)}
.sheet{position:absolute;top:28px;background:var(--paper);box-shadow:0 2px 6px rgba(0,0,0,.25);overflow:hidden}
.sheet-report{left:82px;width:303px;height:1094px}
.sheet-definition{left:483px;width:196px;height:1092px;background:var(--panel-grey)}
.sheet::after{content:"";position:absolute;left:0;right:0;bottom:0;height:4px;background:var(--blue)}
.brand-band{position:absolute;left:0;top:0;width:100%;background:var(--blue);display:flex;align-items:center;justify-content:center;gap:6px;color:#fff}
.sheet-report .brand-band{height:72px;border-top:4px solid #2a6fd0}
.sheet-definition .brand-band{height:48px}
.brand-mark{width:14px;height:14px;border-radius:50%;background:#fff}
.brand-name{font-family:"Montserrat",sans-serif;font-weight:700;font-size:22px;letter-spacing:.2px}
.sheet-definition .brand-name{font-size:15px}
.sheet-definition .brand-mark{width:10px;height:10px}
.band-notch{position:absolute;left:50%;top:46px;width:0;height:0;border-left:8px solid transparent;border-right:8px solid transparent;border-top:7px solid var(--blue);transform:translateX(-50%)}
.sheet-label{position:absolute;top:1140px;font-family:"Montserrat",sans-serif;font-weight:800;font-size:29px;color:var(--navy);letter-spacing:.5px;transform:translateX(-50%)}

/* region blocks */
.region{position:absolute;left:8px;width:288px;border:1px solid #222;background:#fff}
.region-title{position:absolute;top:-5px;left:50%;transform:translateX(-50%);background:#fff;padding:0 3px;font:700 7px "Montserrat",sans-serif;white-space:nowrap}
.tag{position:absolute;left:4px;height:8px;background:var(--blue);border-radius:4px;color:#fff;font:700 3.6px "Open Sans",sans-serif;display:flex;align-items:center;gap:3px;padding:0 6px 0 1px;white-space:nowrap}
.tag-num{width:6px;height:6px;border-radius:50%;background:#fff;color:var(--blue);display:flex;align-items:center;justify-content:center;font-size:3.6px}
.data-table{position:absolute;left:8px;width:272px;border:1px solid var(--blue);box-shadow:0 1px 2px rgba(0,0,0,.2);display:grid;font-size:5px;text-align:center}
.data-table .th{background:var(--blue);color:#fff;font-size:3.3px;line-height:1.2;padding:1px;height:14px;display:flex;align-items:center;justify-content:center;border-right:1px solid #fff;overflow:hidden}
.data-table .td{height:14px;display:flex;align-items:center;justify-content:center}
.data-table .tiny{font-size:3.3px;line-height:1.2}
.cols-8{grid-template-columns:repeat(8,1fr)}
.cols-4{grid-template-columns:1fr 1fr 1fr 1fr}
.cols-3{grid-template-columns:1.2fr 1.3fr 1fr}

/* memphis */
.memphis{position:absolute;left:0;top:674px;width:303px;height:256px;background:var(--blue);clip-path:polygon(0 0,46% 0,50% 4%,54% 0,100% 0,100% 89%,0 100%)}
.memphis-stripe{position:absolute;left:0;width:303px;background:var(--blue-dark)}
.chevron{position:absolute;left:50%;width:7px;height:7px;border-right:1px solid var(--blue);border-bottom:1px solid var(--blue);transform:translateX(-50%) rotate(45deg)}
.section-title{position:absolute;left:0;height:14px;display:flex;align-items:center;padding-left:6px;font:700 7px "Montserrat",sans-serif;white-space:nowrap}
.memphis-title{top:701px;width:108px;background:#fff;color:var(--blue);clip-path:polygon(0 0,100% 0,94% 100%,0 100%)}
.m-head{position:absolute;top:726px;left:72px;display:grid;grid-template-columns:repeat(8,27px);gap:1px}
.m-head span{background:#fff;color:var(--blue);font-size:2.8px;line-height:1.2;height:11px;display:flex;align-items:center;justify-content:center;text-align:center}
.m-row{position:absolute;left:6px;display:flex;align-items:center;gap:3px;color:#fff;font:700 3.6px "Open Sans",sans-serif;line-height:1.25;width:62px;transform:translateY(-50%)}
.m-row-num{width:7px;height:7px;flex:none;border-radius:50%;background:#fff;color:var(--blue);display:flex;align-items:center;justify-content:center;font-size:3.6px}
.m-val{position:absolute;color:#fff;font-size:4px;width:27px;text-align:center;line-height:1.2}
.m-small{font-size:3px;font-weight:700}
.fy{position:absolute;background:#fff;color:var(--blue);font-size:2.6px;border-radius:2px;padding:1px 2px;white-space:nowrap}
.m-axis{position:absolute;left:9px;top:756px;width:1px;height:138px;background:rgba(255,255,255,.7)}

/* combined */
.combined-title{top:942px;width:297px;background:var(--blue);color:#fff;font-size:6px;clip-path:polygon(0 0,100% 0,97% 100%,0 100%)}
.combined-axis{position:absolute;left:13px;top:962px;width:1px;height:100px;background:var(--blue)}
.c-row{position:absolute;left:9px;width:286px;height:18px;border-bottom:1px dotted #c9d6ea;display:flex;align-items:center}
.c-num{width:8px;height:8px;border-radius:50%;background:#fff;border:1px solid var(--blue);color:var(--blue);font-size:4px;font-weight:700;display:flex;align-items:center;justify-content:center;flex:none}
.c-label{margin-left:5px;width:95px;font:700 3.8px "Open Sans",sans-serif;line-height:1.25}
.c-value{font-size:4.6px;color:var(--blue);margin-left:10px}

/* definition */
.def-heading{position:absolute;top:58px;width:100%;text-align:center;font:600 6px "Montserrat",sans-serif;color:var(--navy)}
.def-heading b{color:var(--blue)}
.step-one{position:absolute;left:85px;top:77px;width:26px;height:26px;border-radius:50%;border:2px solid var(--navy);background:#fff;color:var(--navy);font:800 14px "Montserrat",sans-serif;display:flex;align-items:center;justify-content:center}
.def-intro{position:absolute;left:8px;top:107px;width:180px;text-align:center;font:600 4.8px "Open Sans",sans-serif;line-height:1.35;color:#333}
.cell-row{position:absolute;left:0;width:196px;height:28px}
.cell-line{position:absolute;left:10px;top:13px;width:34px;height:3px;border-radius:2px;background:var(--c)}
.cell-dot{position:absolute;left:38px;top:11px;width:7px;height:7px;border-radius:50%;background:#fff;border:2px solid var(--c)}
.cell-pill{position:absolute;left:62px;top:1px;width:126px;height:26px;background:#fff;border-radius:13px;box-shadow:0 1px 3px rgba(0,0,0,.15);padding:4px 6px 0 20px;font-size:3px;line-height:1.3;color:#444;display:flex;align-items:center}
.cell-badge{position:absolute;left:48px;top:0;width:28px;height:28px;border-radius:50%;background:var(--c);display:flex;align-items:center;justify-content:center}
.cell-badge span{width:21px;height:21px;border-radius:50%;background:#fff;border:2px solid var(--c);color:var(--navy);font:800 10px "Montserrat",sans-serif;display:flex;align-items:center;justify-content:center}
.hub{position:absolute;left:47px;top:532px;width:104px;height:104px;border-radius:50%;background:conic-gradient(from 100deg,var(--blue-light) 0 90deg,var(--red) 90deg 160deg,var(--yellow) 160deg 230deg,#fff 230deg);padding:5px;box-shadow:0 2px 5px rgba(0,0,0,.2)}
.hub-face{width:100%;height:100%;border-radius:50%;background:#fff;text-align:center;padding:12px 9px 0}
.hub-num{font:800 22px "Montserrat",sans-serif;color:var(--blue);line-height:1}
.hub-text{font:700 3.6px "Open Sans",sans-serif;color:var(--blue);line-height:1.3;margin-top:3px}
.capsule{position:absolute;top:660px;width:36px;height:92px;border-radius:18px;background:#fff;box-shadow:0 2px 4px rgba(0,0,0,.18);border-top:4px solid var(--c);text-align:center;padding:4px 3px 0}
.capsule-letter{width:18px;height:18px;margin:0 auto;border-radius:50%;border:2px solid var(--c);color:var(--navy);font:800 8px "Montserrat",sans-serif;display:flex;align-items:center;justify-content:center}
.capsule-text{margin-top:6px;font:700 2.9px "Open Sans",sans-serif;line-height:1.3;color:var(--blue)}
.step-banner{position:absolute;height:26px;background:var(--c);color:#fff;font:700 3px "Open Sans",sans-serif;line-height:1.3;display:flex;flex-direction:column;justify-content:center;text-align:center;padding:0 8px;box-shadow:0 1px 3px rgba(0,0,0,.2)}
.banner-right{left:92px;width:96px;border-radius:0 13px 13px 0}
.banner-left{left:10px;width:96px;border-radius:13px 0 0 13px}
.step-node{position:absolute;width:44px;height:44px;border-radius:50%;background:var(--c);display:flex;align-items:center;justify-content:center;box-shadow:0 2px 4px rgba(0,0,0,.2)}
.step-node span{width:34px;height:34px;border-radius:50%;background:#fff;color:var(--c);font:800 18px "Montserrat",sans-serif;display:flex;align-items:center;justify-content:center}
</style>
</head>
<body>

<section class="sheet sheet-report" aria-label="Packet report">
  <header class="brand-band"><span class="brand-mark"></span><span class="brand-name">Bright Sprout</span></header>

  <div class="region" style="top:85px;height:284px">
    <div class="region-title">NASHVILLE</div>
    <div class="tag" style="top:12px"><span class="tag-num">1</span>AX SYSTEM VS. PACKET TRACKING SYSTEM</div>
    <div class="data-table cols-8" style="top:29px">
      <div class="th">CALL CENTER PACKETS</div><div class="th">COMPLETE PACKETS</div><div class="th">DUPLICATES PACKETS</div><div class="th">INCOMPLETE PACKETS</div><div class="th">NO SIGNATURE PACKETS</div><div class="th">DECLINE PACKETS</div><div class="th">BLANKS PACKETS</div><div class="th">(OVER)/UNDER ESTIMATED</div>
      <div class="td">49</div><div class="td">22,454</div><div class="td">468</div><div class="td">919</div><div class="td">-</div><div class="td">1034</div><div class="td">489</div><div class="td">-</div>
      <div class="td"></div><div class="td"></div><div class="td tiny">TOTAL PACKETS</div><div class="td">25,364</div><div class="td tiny">PACKETS TRACKING SYSTEM</div><div class="td">23,349</div><div class="td">489</div><div class="td">2,015</div>
    </div>
    <div class="tag" style="top:93px"><span class="tag-num">2</span>INSURED PACKETS</div>
    <div class="data-table cols-4" style="top:110px">
      <div class="th">CALL CENTER PACKETS</div><div class="th">COMPLETE PACKETS</div><div class="th">DUPLICATES PACKETS</div><div class="th">UNINSURED PACKETS</div>
      <div class="td">49</div><div class="td">22,405</div><div class="td"></div><div class="td">5944</div>
      <div class="td"></div><div class="td tiny">INSURED PACKETS</div><div class="td">16,510</div><div class="td"></div>
    </div>
    <div class="tag" style="top:173px"><span class="tag-num">3</span>INSURED COMPLETED EXAMS OUT OF COMPLETED PACKETS &nbsp;- &nbsp;3,718</div>
    <div class="tag" style="top:199px"><span class="tag-num">4</span>LEFT BEHIND/TO COMPLETE &nbsp;- &nbsp;12,792</div>
    <div class="tag" style="top:222px"><span class="tag-num">5</span>COMPARISON OF INSURED PACKETS 2017-18 VS. 2018-19</div>
    <div class="data-table cols-3" style="top:239px">
      <div class="th">2017 - 2018</div><div class="th">2018 - 2019</div><div class="th">DIFFERENCE</div>
      <div class="td" style="height:24px">22,354</div><div class="td" style="height:24px">16,510</div><div class="td" style="height:24px">5,844</div>
    </div>
  </div>

  <div class="region" style="top:386px;height:274px">
    <div class="region-title">KNOXVILLE</div>
    <div class="tag" style="top:12px"><span class="tag-num">1</span>AX SYSTEM VS. PACKET TRACKING SYSTEM</div>
    <div class="data-table cols-8" style="top:29px">
      <div class="th">CALL CENTER PACKETS</div><div class="th">COMPLETE PACKETS</div><div class="th">DUPLICATES PACKETS</div><div class="th">INCOMPLETE PACKETS</div><div class="th">NO SIGNATURE PACKETS</div><div class="th">DECLINE PACKETS</div><div class="th">BLANKS PACKETS</div><div class="th">(OVER)/UNDER ESTIMATED</div>
      <div class="td">49</div><div class="td">22,454</div><div class="td">468</div><div class="td">919</div><div class="td">-</div><div class="td">1034</div><div class="td">489</div><div class="td">-</div>
      <div class="td"></div><div class="td"></div><div class="td tiny">TOTAL PACKETS</div><div class="td">25,364</div><div class="td tiny">PACKETS TRACKING SYSTEM</div><div class="td">23,349</div><div class="td">489</div><div class="td">2,015</div>
    </div>
    <div class="tag" style="top:93px"><span class="tag-num">2</span>INSURED PACKETS</div>
    <div class="data-table cols-4" style="top:110px">
      <div class="th">CALL CENTER PACKETS</div><div class="th">COMPLETE PACKETS</div><div class="th">DUPLICATES PACKETS</div><div class="th">UNINSURED PACKETS</div>
      <div class="td">49</div><div class="td">22,405</div><div class="td"></div><div class="td">5944</div>
      <div class="td"></div><div class="td tiny">INSURED PACKETS</div><div class="td">16,510</div><div class="td"></div>
    </div>
    <div class="tag" style="top:173px"><span class="tag-num">3</span>INSURED COMPLETED EXAMS OUT OF COMPLETED PACKETS &nbsp;- &nbsp;3,718</div>
    <div class="tag" style="top:199px"><span class="tag-num">4</span>LEFT BEHIND/TO COMPLETE &nbsp;- &nbsp;12,792</div>
    <div class="tag" style="top:222px"><span class="tag-num">5</span>COMPARISON OF INSURED PACKETS 2017-18 VS. 2018-19</div>
    <div class="data-table cols-3" style="top:239px">
      <div class="th">2017 - 2018</div><div class="th">2018 - 2019</div><div class="th">DIFFERENCE</div>
      <div class="td">22,354</div><div class="td">16,510</div><div class="td">5,844</div>
    </div>
  </div>

  <div class="memphis">
    <div class="memphis-stripe" style="top:110px;height:34px"></div>
    <div class="memphis-stripe" style="top:178px;height:28px"></div>
  </div>
  <div class="chevron" style="top:686px;border-color:#fff"></div>
  <div class="section-title memphis-title">MEMPHIS MOBILE / CLINICS</div>
  <div class="m-head">
    <span>CALL CENTER PACKETS</span><span>COMPLETE PACKETS</span><span>DUPLICATES PACKETS</span><span>INCOMPLETE PACKETS</span><span>NO SIGNATURE PACKETS</span><span>DECLINE PACKETS</span><span>BLANKS PACKETS</span><span>(OVER)/UNDER ESTIMATED</span>
  </div>
  <div class="m-axis"></div>

  <div class="m-row" style="top:759px"><span class="m-row-num">1</span>AX SYSTEM VS. PACKET TRACKING SYSTEM</div>
  <div class="m-val" style="left:72px;top:744px">13984</div><div class="m-val" style="left:100px;top:744px">15843</div><div class="m-val" style="left:128px;top:744px">2776</div><div class="m-val" style="left:156px;top:744px">1646</div><div class="m-val" style="left:212px;top:744px">2776</div><div class="m-val" style="left:240px;top:744px">384</div>
  <div class="m-val m-small" style="left:124px;top:760px;width:35px">TOTAL PACKETS</div><div class="m-val" style="left:156px;top:760px">29,827</div><div class="m-val m-small" style="left:181px;top:758px;width:33px">TOTAL PACKETS TRACKING SYSTEM</div><div class="m-val" style="left:212px;top:760px">37409</div><div class="m-val" style="left:268px;top:760px">7582</div>

  <div class="m-row" style="top:795px"><span class="m-row-num">2</span>INSURED PACKETS</div>
  <div class="m-val" style="left:72px;top:792px">13984</div><div class="m-val" style="left:100px;top:792px">15843</div><div class="m-val" style="left:156px;top:792px">1646</div><div class="m-val" style="left:268px;top:792px">7361</div>
  <div class="m-val m-small" style="left:100px;top:806px">INSURED PACKETS</div><div class="m-val" style="left:128px;top:807px">22,466</div>

  <div class="m-row" style="top:836px"><span class="m-row-num">3</span>INSURED COMPLETED EXAMS OUT OF COMPLETED PACKETS</div>
  <div class="m-val" style="left:128px;top:835px">6107</div>

  <div class="m-row" style="top:866px"><span class="m-row-num">4</span>LEFT BEHIND / TO COMPLETE</div>
  <div class="m-val" style="left:128px;top:861px">16359</div>

  <div class="m-row" style="top:893px"><span class="m-row-num">5</span>COMPARISON OF INSURED PACKETS</div>
  <div class="m-val" style="left:72px;top:887px">30538</div><div class="m-val" style="left:100px;top:887px">22466</div><div class="m-val" style="left:128px;top:887px">8072</div>
  <span class="fy" style="left:76px;top:899px">FY 2017-18</span><span class="fy" style="left:104px;top:899px">FY 2018-19</span>

  <div class="chevron" style="top:924px"></div>

  <div class="section-title combined-title">COMBINED NEED ANALYSIS MEMPHIS MOBILE/CLINICS, NASHVILLE, KNOXVILLE</div>
  <div class="combined-axis"></div>
  <div class="c-row" style="top:961px"><span class="c-num">1</span><span class="c-label">TOTAL GROSS PACKETS RECEIVED STATEWIDE</span><span class="c-value">55,191</span></div>
  <div class="c-row" style="top:993px"><span class="c-num">2</span><span class="c-label">TOTAL INSURED PACKETS RECEIVED STATEWIDE</span><span class="c-value">38,976</span></div>
  <div class="c-row" style="top:1023px"><span class="c-num">3</span><span class="c-label">STATEWIDE EPSDT NEEDS FOR INSURED PACKETS</span><span class="c-value">13,916</span></div>
  <div class="c-row" style="top:1050px;height:24px"><span class="c-num">4</span><span class="c-label">GROSS PACKET NEEDS TO CONVERT INTO INSURED PACKETS @ 29% OF STEP 6</span><span class="c-value">17,952</span></div>
</section>

<section class="sheet sheet-definition" aria-label="Definitions legend">
  <header class="brand-band"><span class="brand-mark"></span><span class="brand-name">Bright Sprout</span></header>
  <div class="band-notch"></div>
  <div class="def-heading"><b>DEFINTIONS OF STAGES</b> FOR A PACKET</div>
  <div class="step-one">1</div>
  <p class="def-intro">This represents the comparisons of Completed Packets in AX vs Packet Tracking Gross Packets Received by Outreach</p>

  <div class="cell-row" style="top:132px;--c:var(--blue-light)"><span class="cell-line"></span><span class="cell-dot"></span><div class="cell-pill">Cell C4/27 "Call Center" reflects the number of Call Center Packets Completed</div><div class="cell-badge"><span>A</span></div></div>
  <div class="cell-row" style="top:168px;--c:var(--red)"><span class="cell-line"></span><span class="cell-dot"></span><div class="cell-pill">Cell D4/27 "Complete Packets" reflects the number of Packets completing the HIC Cycle for patient to become available for EPSDT Screenings</div><div class="cell-badge"><span>B</span></div></div>
  <div class="cell-row" style="top:204px;--c:var(--yellow)"><span class="cell-line"></span><span class="cell-dot"></span><div class="cell-pill">Cell E4/27 "Duplicate Packets" defined as packets scanned that may have more than one packet scanned into AX</div><div class="cell-badge"><span>C</span></div></div>
  <div class="cell-row" style="top:241px;--c:var(--green)"><span class="cell-line"></span><span class="cell-dot"></span><div class="cell-pill">Cell F4/27 "Incomplete Packets" is not scanned into AX, missing child history; located on the follow-up shelf for the call center to contact guardian</div><div class="cell-badge"><span>D</span></div></div>
  <div class="cell-row" style="top:277px;--c:var(--blue-light)"><span class="cell-line"></span><span class="cell-dot"></span><div class="cell-pill">Cell G4/27 "Complete Packets" reflects the number of Packets completing the HIC Cycle for patient to become available for EPSDT Screenings</div><div class="cell-badge"><span>E</span></div></div>
  <div class="cell-row" style="top:313px;--c:var(--red)"><span class="cell-line"></span><span class="cell-dot"></span><div class="cell-pill">Cell H4/27 "Declined Packet" guardian writes decline service on the packet and this packet is not scanned into AX</div><div class="cell-badge"><span>F</span></div></div>
  <div class="cell-row" style="top:350px;--c:var(--yellow)"><span class="cell-line"></span><span class="cell-dot"></span><div class="cell-pill">Cell I4/27 "Blanks" is a completely blank packet and is not scanned into AX system</div><div class="cell-badge"><span>G</span></div></div>
  <div class="cell-row" style="top:386px;--c:var(--green)"><span class="cell-line"></span><span class="cell-dot"></span><div class="cell-pill">Cell F5/26 "Total Packets = Call Center Packet + Complete Packets"</div><div class="cell-badge"><span>H</span></div></div>
  <div class="cell-row" style="top:422px;--c:var(--blue-light)"><span class="cell-line"></span><span class="cell-dot"></span><div class="cell-pill">Cell F5/26 "Total Packets = Call Center Packet + Complete Packets"</div><div class="cell-badge"><span>I</span></div></div>
  <div class="cell-row" style="top:459px;--c:var(--red)"><span class="cell-line"></span><span class="cell-dot"></span><div class="cell-pill">Cell G5/26 "Packet Tracking System" reflects the number estimated out of the tracking system, includes Call Center, Complete, Duplicate, Incomplete, No Signature, Declines and Blanks</div><div class="cell-badge"><span>J</span></div></div>
  <div class="cell-row" style="top:495px;--c:var(--yellow)"><span class="cell-line"></span><span class="cell-dot"></span><div class="cell-pill">Cell J5/26 this represents the difference between the AX and Packet Tracking system Over/Under estimates</div><div class="cell-badge"><span>K</span></div></div>

  <svg width="196" height="40" viewBox="0 0 196 40" style="position:absolute;left:0;top:620px" aria-hidden="true">
    <path d="M55 0 Q26 8 26 40 M80 0 Q75 20 75 40 M118 0 Q123 20 122 40 M143 0 Q171 8 171 40" fill="none" stroke="#777" stroke-width=".6" stroke-dasharray="1.5 1.5"/>
  </svg>
  <div class="hub"><div class="hub-face"><div class="hub-num">2</div><p class="hub-text">Insured Packets step gives an forecast of how many insured EPSDT screening from the call center and completed packets minus the uninsured packets received</p></div></div>

  <div class="capsule" style="left:8px;--c:var(--blue-light)"><div class="capsule-letter">A</div><p class="capsule-text">Cell J8/J31 Uninsured packets call center exams completed with no insurance long with no insurance packets received</p></div>
  <div class="capsule" style="left:57px;--c:var(--red)"><div class="capsule-letter">B</div><p class="capsule-text">Cell C31 (Call Center Packets) + D31 (Complete Packets) - F31 (Incomplete) - G31 (no signature) - Minus J31 (uninsured) = Memphis</p></div>
  <div class="capsule" style="left:104px;--c:var(--yellow)"><div class="capsule-letter">C</div><p class="capsule-text">Memphis is calculated by adding back the incomplete and no signature packets per KJP</p></div>
  <div class="capsule" style="left:153px;--c:var(--green)"><div class="capsule-letter">D</div><p class="capsule-text">Cell C8 (Call Center Packets) + D8 (Complete Packets) - Minus J8 (uninsured) = NASH/KNOX</p></div>

  <svg width="196" height="310" viewBox="0 0 196 310" style="position:absolute;left:0;top:770px" aria-hidden="true">
    <g fill="none" stroke-width="9" stroke-linecap="round">
      <path d="M58 18 C90 20 110 40 139 64" stroke="var(--blue-light)"/>
      <path d="M139 64 C110 84 80 90 58 108" stroke="var(--red)"/>
      <path d="M58 108 C90 120 110 136 139 150" stroke="var(--yellow)"/>
      <path d="M139 150 C110 170 80 180 58 198" stroke="var(--green)"/>
      <path d="M58 198 C90 210 110 228 139 242" stroke="var(--red)"/>
      <path d="M139 242 C110 262 80 268 58 282" stroke="var(--yellow)"/>
    </g>
  </svg>

  <div class="step-banner banner-right" style="top:772px;--c:var(--blue-light)"><span>1. NASHVILLE/KNOXVILLE Number of Completed exams for current School Year = 3718</span><span>2. MEMPHIS/CLINIC Number of Completed exams for current School Year = 6107</span></div>
  <div class="step-node" style="left:36px;top:766px;--c:var(--blue-light)"><span>3</span></div>
  <div class="step-banner banner-left" style="top:822px;--c:var(--red)"><span>1. NASHVILLE/KNOXVILLE Left Behind to Complete represents the 12,792 EPSDT screening to perform</span><span>2. MEMPHIS/CLINIC Left Behind represents the 16,359 screening to perform</span></div>
  <div class="step-node" style="left:117px;top:812px;--c:var(--red)"><span>4</span></div>
  <div class="step-banner banner-right" style="top:864px;--c:var(--yellow)"><span>1. NASHVILLE/KNOXVILLE Comparison of Insured Packets 2017-18 22354 / 2018-19 16510 = 5844</span><span>2. MEMPHIS/CLINIC 2017-18 30538 / 2018-19 22466 = 8072</span></div>
  <div class="step-node" style="left:36px;top:856px;--c:var(--yellow)"><span>5</span></div>
  <div class="step-banner banner-left" style="top:908px;--c:var(--green)"><span>Total gross packets received statewide = MEM + NASH</span></div>
  <div class="step-node" style="left:117px;top:898px;--c:var(--green)"><span>6</span></div>
  <div class="step-banner banner-right" style="top:954px;--c:var(--red)"><span>Total Insured packets received statewide = MEM + NASH</span></div>
  <div class="step-node" style="left:36px;top:946px;--c:var(--red)"><span>7</span></div>
  <div class="step-banner banner-left" style="top:1000px;--c:var(--yellow)"><span>Statewide EPSDT Needs for Insured Packets = E16 + E22</span></div>
  <div class="step-node" style="left:117px;top:990px;--c:var(--yellow)"><span>8</span></div>
  <div class="step-banner banner-right" style="top:1040px;--c:var(--teal)"><span>Gross Packet Needs to convert into Insured Packets @ 29% of Step 6</span></div>
  <div class="step-node" style="left:36px;top:1030px;--c:var(--teal)"><span>9</span></div>
</section>

<div class="sheet-label" style="left:233px">REPORT</div>
<div class="sheet-label" style="left:581px">DEFINITION</div>

</body>
</html>
```